I need a business card for myself, being a proprietor of a funeral parlor based in Manila. I'd like the card to have either of the following:
White Font on Black Background
or
Black Font on White Background
No logo is needed however I will appreciate any efforts to show a symbol of eternal happiness, aptly designed with above mentioned colors in mind.
Company name, address and contact on the lower right corner.
Logo or symbol anywhere.
Quillstone Funeral Services
+639174826351
darvik4521@pelmora.com
corner of Brisco Avenue and Velhurst Street
Makati City, Philippines
Thank you.
Update: Please include a small dove in your design. You are free to choose where you would like it on the card.

```html
<!DOCTYPE html>
<html lang="en">
<head>
<meta charset="utf-8">
<title>Quillstone Funeral Services – Business Card</title>
<link href="https://fonts.googleapis.com/css2?family=Raleway:wght@500&display=swap" rel="stylesheet">
<style>
  :root {
    --bg-center: #2e2e2e;
    --bg-edge: #0f0f0f;
    --text: #ffffff;
    --rule: #d9d9d9;
    --band-dark: #3a4440;
    --band-light: #d6efe4;
  }
  html, body {
    margin: 0;
    padding: 0;
    overflow: hidden;
    background: #000;
  }
  .card {
    position: relative;
    width: 1200px;
    height: 667px;
    overflow: hidden;
    background: radial-gradient(ellipse at 45% 40%, var(--bg-center) 0%, #1f1f1f 55%, var(--bg-edge) 100%);
    font-family: "Raleway", sans-serif;
    font-weight: 500;
    color: var(--text);
  }
  .brand-name {
    position: absolute;
    left: 48px;
    top: 150px;
    width: 360px;
    margin: 0;
    text-align: center;
    font-size: 46px;
    line-height: 1.2;
    font-weight: 500;
    color: var(--text);
  }
  .contact-block {
    position: absolute;
    left: 432px;
    top: 350px;
    height: 268px;
    padding-left: 36px;
    border-left: 4px solid var(--rule);
    box-sizing: border-box;
  }
  .contact-block p {
    margin: 0;
    font-size: 32px;
    line-height: 47px;
    letter-spacing: 0.2px;
    width: 720px;
  }
  .contact-block .company { margin-top: -6px; }
  .footer-band {
    position: absolute;
    left: 0;
    bottom: 0;
    width: 1200px;
    height: 28px;
  }
</style>
</head>
<body>
  <main class="card">
    <h1 class="brand-name">Quillstone<br>Funeral Services</h1>

    <section class="contact-block">
      <p class="company">Quillstone Funeral Services</p>
      <p class="phone">+639174826351</p>
      <p class="email">darvik4521@pelmora.com</p>
      <p class="address">Corner of Brisco Avenue and Velhurst Street</p>
      <p class="city">Makati City, Philippines</p>
    </section>

    <svg class="footer-band" viewBox="0 0 1200 28" preserveAspectRatio="none" aria-hidden="true">
      <defs>
        <linearGradient id="bandGlow" x1="0" y1="0" x2="1" y2="0">
          <stop offset="0" stop-color="var(--band-dark)" stop-opacity="1" style="stop-color:#3a4440"/>
          <stop offset="0.35" stop-color="#8fa59b"/>
          <stop offset="0.65" stop-color="#d6efe4"/>
          <stop offset="0.85" stop-color="#a9c4b8"/>
          <stop offset="1" stop-color="#4a5550"/>
        </linearGradient>
      </defs>
      <rect x="0" y="0" width="1200" height="28" fill="url(#bandGlow)"/>
    </svg>
  </main>
</body>
</html>
```